Torvale Works- Plumbing Business Card

We need a business card design for a new company that services Canberra and surrounds. We are a professional family-owned plumbing company who has 20+ years' experience. We would like to use our logo as well as the colours black, white, grey and the signature green. The final design needs to communicate professional, high-end, plumbing with reliable service. We provide obligation free quotes and are open 24/7. Services include: Bathroom/kitchen renovations, drainage, stormwater, water leaks, plumbing maintenance, water tanks and septics.

Target Market(s)

Homeowners, real estate agents, builders, small business owners

Industry/Entity Type

Plumbing & Construction

Font styles to use
Serif
Sans Serif

Colors
59FF00
82FF00
B8FF75
E3FFCB
F4FFEA

Requirements
Must have
• Must have logo, example of services and contact details

```html
<!DOCTYPE html>
<html lang="en">
<head>
<meta charset="utf-8">
<title>Torvale Works – Business Card</title>
<link rel="stylesheet" href="https://fonts.googleapis.com/css2?family=League+Spartan:wght@700&family=Roboto:wght@400;900&display=swap">
<style>
  :root {
    --green: #18a44b;
    --charcoal: #3a3a3c;
    --black: #07090a;
    --white: #ffffff;
    --page: #ffffff;
  }
  html, body {
    margin: 0;
    width: 1009px;
    height: 1200px;
    overflow: hidden;
    background: var(--page);
  }
  .stage {
    position: relative;
    width: 1200px;
    height: 1427px;
    transform: scale(0.840833);
    transform-origin: 0 0;
    font-family: "Roboto", Arial, sans-serif;
  }
  .card {
    position: absolute;
    left: 123px;
    width: 955px;
    height: 545px;
    background: var(--white);
    overflow: hidden;
    box-shadow: 12px 14px 22px rgba(0,0,0,0.28);
  }
  .card--front { top: 128px; }
  .card--back  { top: 754px; height: 546px; }
  .card__shapes { position: absolute; inset: 0; }

  .brand {
    position: absolute;
    margin: 0;
    color: var(--green);
    font-family: "Roboto", Arial, sans-serif;
    font-weight: 900;
    text-transform: uppercase;
    line-height: 0.95;
    text-align: right;
  }
  .card--front .brand { right: 40px; top: 40px; font-size: 46px; }
  .card--back .brand  { right: 48px; top: 60px; font-size: 96px; }

  .holder {
    position: absolute;
    left: 60px;
    top: 180px;
    margin: 0;
    font-family: "League Spartan", "Helvetica Neue", sans-serif;
    font-weight: 700;
    font-size: 72px;
    letter-spacing: 0.5px;
    color: var(--charcoal);
    line-height: 1;
  }
  .holder__rule {
    position: absolute;
    left: 60px;
    top: 257px;
    width: 495px;
    height: 6px;
    background: var(--green);
  }

  .contact {
    position: absolute;
    list-style: none;
    margin: 0;
    padding: 0;
    color: var(--white);
    font-size: 27px;
  }
  .contact li {
    display: flex;
    align-items: center;
    height: 46px;
  }
  .contact svg { width: 34px; height: 34px; margin-right: 16px; flex: none; }
  .contact--left  { left: 58px;  top: 392px; }
  .contact--right { left: 523px; top: 393px; }
  .contact__rule {
    position: absolute;
    left: 53px;
    top: 508px;
    width: 849px;
    height: 6px;
    background: var(--white);
  }

  .services {
    position: absolute;
    margin: 0;
    padding: 0;
    list-style: none;
    color: var(--white);
    font-size: 28px;
  }
  .services li {
    position: relative;
    padding-left: 24px;
    height: 43px;
    line-height: 43px;
  }
  .services li::before {
    content: "";
    position: absolute;
    left: 0;
    top: 16px;
    width: 11px;
    height: 11px;
    border-radius: 50%;
    background: var(--white);
  }
  .services--left  { left: 50px;  top: 376px; }
  .services--right { left: 550px; top: 376px; }
</style>
</head>
<body>
<main class="stage">

  <section class="card card--front" aria-label="Card front">
    <svg class="card__shapes" viewBox="0 0 955 545" preserveAspectRatio="none" aria-hidden="true">
      <path fill="var(--charcoal)" d="M0 0 H663 C600 45 520 100 400 95 C330 92 280 75 220 82 C120 95 40 150 0 207 Z"/>
      <path fill="var(--green)" d="M0 377 C120 330 260 300 400 325 C520 348 600 372 720 362 C840 352 920 250 955 167 V545 H0 Z"/>
    </svg>

    <p class="brand">Torvale<br>Works</p>

    <h1 class="holder">MARCUS HALE</h1>
    <div class="holder__rule"></div>

    <ul class="contact contact--left">
      <li>
        <svg viewBox="0 0 34 34" aria-hidden="true"><circle cx="17" cy="17" r="16" fill="var(--white)"/><path fill="var(--green)" d="M17 7a7 7 0 0 0-7 7c0 5 7 13 7 13s7-8 7-13a7 7 0 0 0-7-7zm0 9.5a2.5 2.5 0 1 1 0-5 2.5 2.5 0 0 1 0 5z"/></svg>
        TVW Plumbing Canberra
      </li>
      <li>
        <svg viewBox="0 0 34 34" aria-hidden="true"><circle cx="17" cy="17" r="16" fill="var(--white)"/><path fill="var(--green)" d="M12 8l3 5-2 2c1 3 3 5 6 6l2-2 5 3-2 4c-8 0-15-7-15-15z"/></svg>
        0400 318 924
      </li>
    </ul>

    <ul class="contact contact--right">
      <li>
        <svg viewBox="0 0 34 34" aria-hidden="true"><circle cx="17" cy="17" r="16" fill="var(--white)"/><rect x="9" y="11" width="16" height="12" rx="1.5" fill="var(--green)"/><path d="M9.5 12l7.5 6 7.5-6" fill="none" stroke="var(--white)" stroke-width="1.6"/></svg>
        info@torvaleworks.com
      </li>
      <li>
        <svg viewBox="0 0 34 34" aria-hidden="true"><circle cx="17" cy="17" r="16" fill="var(--white)"/><g fill="none" stroke="var(--green)" stroke-width="1.6"><circle cx="17" cy="17" r="8"/><ellipse cx="17" cy="17" rx="3.5" ry="8"/><path d="M9 17h16M10.5 13h13M10.5 21h13"/></g></svg>
        torvaleworks.com.au
      </li>
    </ul>
    <div class="contact__rule"></div>
  </section>

  <section class="card card--back" aria-label="Card back">
    <svg class="card__shapes" viewBox="0 0 955 546" preserveAspectRatio="none" aria-hidden="true">
      <path fill="var(--charcoal)" d="M0 0 H275 C180 70 85 150 92 235 C98 290 135 322 165 335 L0 335 Z"/>
      <path fill="var(--black)" d="M0 0 H175 C115 60 70 170 80 240 C88 290 130 325 165 335 L0 335 Z"/>
      <path fill="var(--green)" d="M0 195 C40 260 100 315 165 335 C280 370 420 362 560 337 C700 312 820 320 955 383 V546 H0 Z"/>
    </svg>

    <p class="brand">Torvale<br>Works</p>

    <ul class="services services--left">
      <li>Bathroom/Kitchen Renovations</li>
      <li>Drainage</li>
      <li>Plumbing Maintenance</li>
    </ul>
    <ul class="services services--right">
      <li>Stormwater</li>
      <li>Water Leaks</li>
      <li>Water Tanks and Septics</li>
    </ul>
  </section>

</main>
</body>
</html>
```